Website for Dental Office - The Brightcrest Clinic

The brightcrest clinic is a dental office offering cosmetic dentistry, general dentistry, and multi-specialty dental care all under one roof in our state-of-the-art cosmetic dental center. We are particularly striving to provide services that fit the need of the young generation. Thus, we hope to have a modern, professional concise website that represents our spirit.

*Should be able to switch from English to Chinese

6 sections besides homepage:
Home, Meet us, Services,
Patient Info, Cases&Reviews, Blog, Contact

The Services sections should contain multiple subsections such as cleaning and prevention, cosmetic dentistry, implant dentistry, removable dentures, etc...
The Patient Info section is also intended to contain several subsections such as
New Patient offer, accepted Insurance, patient portal, helpful tips, etc...

Target Market(s)

young generation

Coding

Number of Pages Required

5+ page

Font styles to use
Sans Serif

Colors
0592cd
33a6d7
85cae6
00a990
33b8a4
86cfc6
cee9f5
cfeae6
3277b5

Requirements
Must have
• *Should be able to switch from English to Chinese
Nice to have
• http://www.thebrightcrestclinic-example.com/
• As a reference, the above link is the current website, but we would like to change the appearance and the content (our new logo's picture is attached)

```html
<!DOCTYPE html>
<html lang="en">
<head>
<meta charset="utf-8">
<title>The Brightcrest Clinic</title>
<link rel="stylesheet" href="https://fonts.googleapis.com/css2?family=Lato:wght@400;700;900&display=swap">
<style>
:root{
  --blue:#0592cd;--blue-mid:#33a6d7;--blue-light:#85cae6;--blue-pale:#cee9f5;
  --teal:#00a990;--teal-mid:#33b8a4;--teal-light:#86cfc6;--navy:#3277b5;
  --ink:#222;--text:#444;--dark:#111;
}
*{margin:0;padding:0;box-sizing:border-box}
html,body{width:1200px;height:4445px;overflow:hidden;background:#fff}
body{font-family:'Lato',sans-serif;color:var(--text);position:relative}
.abs{position:absolute}
.btn{position:absolute;display:flex;align-items:center;justify-content:center;gap:10px;background:var(--blue-mid);color:#fff;font-weight:700;font-size:18px;border-radius:30px;text-decoration:none}
.btn .dot{width:15px;height:15px;border-radius:50%;background:#fff;position:relative}
.btn .dot::after{content:"";position:absolute;left:4px;top:4px;border-left:7px solid var(--blue-mid);border-top:4px solid transparent;border-bottom:4px solid transparent}
.rule{position:absolute;height:4px;width:50px;background:var(--blue)}
.rule.white{background:#fff}

/* top bar */
.topbar{top:0;left:0;width:1200px;height:45px;background:var(--navy);color:#fff;font-size:15px;font-weight:700}
.topbar span{position:absolute;top:13px}
.topbar .sep{position:absolute;top:0;width:1px;height:45px;background:rgba(255,255,255,.3)}
.social{position:absolute;width:16px;height:16px;border-radius:50%;border:2px solid #fff}

/* nav */
.nav{top:45px;left:0;width:1200px;height:88px;background:#fff}
.brand{position:absolute;display:flex;align-items:center;gap:12px;font-weight:900;color:var(--blue-mid);line-height:1}
.brand .mark{background:var(--blue-mid);border-radius:6px}
.menu{position:absolute;top:36px;left:414px;display:flex;gap:23px;font-size:16px;font-weight:700;color:var(--ink)}
.menu .on{color:var(--blue-mid)}

/* hero */
.hero{top:133px;left:0;width:1200px;height:620px;background:linear-gradient(100deg,#4f5a3f 0%,#7b7656 35%,#c8b7a2 65%,#efe7dc 100%)}
.hero h1{position:absolute;left:90px;top:115px;font-size:72px;font-weight:900;color:#fff;line-height:72px}
.hero p{position:absolute;left:90px;top:278px;width:470px;font-size:17px;line-height:30px;color:#fff;font-weight:700}
.circle-btn{position:absolute;width:60px;height:60px;border-radius:50%;background:#fff;border:2px solid var(--teal-mid);display:flex;align-items:center;justify-content:center}

/* about */
.about h2,.blog h2{position:absolute;width:1200px;text-align:center;font-size:46px;font-weight:900;color:var(--ink)}
.about p{position:absolute;left:140px;top:963px;width:920px;text-align:center;font-size:16px;line-height:30px}

/* services */
.services{top:1235px;left:0;width:1200px;height:750px;background:linear-gradient(90deg,#3a4a52,#56636a 50%,#3e4b52)}
.services h2{position:absolute;left:0;width:532px;top:200px;text-align:center;font-size:44px;font-weight:900;color:#fff}
.services p{position:absolute;left:86px;width:360px;top:308px;text-align:center;font-size:15px;line-height:30px;color:#fff}
.tile{position:absolute;width:270px;height:242px;background:linear-gradient(180deg,#1d8fc8,#13a99a);color:#fff;font-size:21px;font-weight:700;text-align:center}
.tile svg{position:absolute;left:105px;top:62px}
.tile span{position:absolute;left:0;width:100%;top:158px}

/* health tips */
.photo{position:absolute}
.tips h2,.offer h2{position:absolute;font-size:44px;font-weight:900}
.tips p{position:absolute;left:715px;top:2222px;width:405px;font-size:15px;line-height:30.5px;text-align:justify}

/* offer */
.offer{top:2567px;left:0;width:1200px;height:650px;background:linear-gradient(90deg,#33b8a4 0%,#2fa8b8 45%,#4a9fd4 100%)}
.offer h2{left:90px;top:130px;color:#fff}
.offer p{position:absolute;left:90px;top:271px;width:405px;font-size:15px;line-height:30.5px;color:#fff;text-align:justify}

/* blog */
.card{position:absolute;top:3398px;width:323px;height:337px;color:#fff;text-align:center}
.card .img{position:absolute;left:9px;top:9px;width:305px;height:200px}
.card h3{position:absolute;top:230px;width:100%;font-size:22px;font-weight:700}
.card p{position:absolute;top:270px;left:15px;width:293px;font-size:15px;line-height:26px}

/* footer */
.footer{top:3850px;left:0;width:1200px;height:595px;background:var(--dark);color:#fff}
.fmenu{position:absolute;top:247px;width:1200px;display:flex;justify-content:center;gap:22px;font-size:16px;font-weight:700}
.ficon{position:absolute;top:308px;width:58px;height:58px;border-radius:50%;display:flex;align-items:center;justify-content:center}
.finfo{position:absolute;top:391px;width:300px;text-align:center;font-size:13px;line-height:24px;font-weight:700}
.flinks{position:absolute;top:488px;width:1200px;text-align:center;font-size:13px}
.copy{position:absolute;top:556px;left:90px;font-size:13px}
</style>
</head>
<body>

<header class="abs topbar">
  <svg class="abs" style="left:90px;top:14px" width="16" height="16" viewBox="0 0 24 24"><path fill="#fff" d="M6.6 10.8a15 15 0 006.6 6.6l2.2-2.2c.3-.3.7-.4 1-.2 1.1.4 2.3.6 3.6.6.6 0 1 .4 1 1V20c0 .6-.4 1-1 1A17 17 0 013 4c0-.6.4-1 1-1h3.5c.6 0 1 .4 1 1 0 1.3.2 2.5.6 3.6.1.3 0 .7-.2 1z"/></svg>
  <span style="left:118px">Call Us : <b style="font-size:19px;font-weight:900">555.014.2290</b></span>
  <div class="sep" style="left:352px"></div>
  <svg class="abs" style="left:384px;top:14px" width="17" height="17" viewBox="0 0 24 24"><path fill="#fff" d="M2 11l20-9-6 20-4-8z"/></svg>
  <span style="left:411px">Email Us : info@brightcrestclinic-example.com</span>
  <div class="sep" style="left:720px"></div>
  <div class="social" style="left:766px;top:14px"></div>
  <div class="social" style="left:809px;top:14px"></div>
  <div class="social" style="left:854px;top:14px"></div>
  <div class="social" style="left:901px;top:14px"></div>
  <div class="sep" style="left:955px"></div>
  <span style="left:989px">English | Chinese</span>
</header>

<nav class="abs nav">
  <div class="brand" style="left:90px;top:18px">
    <div class="mark" style="width:54px;height:50px"></div>
    <div style="font-size:25px">THE BRIGHTCREST<br>CLINIC</div>
  </div>
  <div class="menu">
    <span class="on">HOME</span><span>MEET US</span><span>SERVICES</span><span>PATIENT INFO</span><span>CASES&amp;REVIEWS</span><span>BLOG</span><span>CONTACT</span>
  </div>
</nav>

<section class="abs hero" role="img" aria-label="Photo of a smiling young woman">
  <h1>THE BRIGHTCREST<br>CLINIC</h1>
  <p>Lorem ipsum dolor sit amet, consectetur adipiscing elit, sed do eiusmod tempor incididunt ut labore et dolore magna aliqua.</p>
  <a class="btn" style="left:90px;top:388px;width:198px;height:61px">Get Started <i class="dot"></i></a>
  <svg class="abs" style="left:0;top:540px" width="1200" height="80" viewBox="0 0 1200 80" preserveAspectRatio="none"><path fill="#fff" d="M0 80 L0 77 Q600 -30 1200 72 L1200 80 Z"/></svg>
</section>
<div class="circle-btn" style="left:570px;top:667px">
  <svg width="22" height="22" viewBox="0 0 24 24" fill="none" stroke="var(--blue-mid)" stroke-width="2.5"><path d="M6 5l6 6 6-6M6 12l6 6 6-6"/></svg>
</div>

<section class="about">
  <h2 style="top:845px">ABOUT US</h2>
  <div class="rule" style="left:575px;top:918px"></div>
  <div class="abs" style="left:425px;top:912px;width:352px;height:192px;background:var(--blue-pale);opacity:.6;border-radius:8px"></div>
  <p>Welcome to The Brightcrest Clinic where we specialize in General and Cosmetic Dentistry, Dental Implants, Periodontics (Gum Surgery), Endodontics (Root Canal Treatment) and Reconstructive Dentistry for patients in Boston, Brookline, Cambridge, Brighton, Allston, Newton, Watertown, Wellesley and all other surrounding neighborhoods of Boston, Massachusetts.</p>
  <a class="btn" style="left:518px;top:1088px;width:164px;height:47px">Read More <i class="dot"></i></a>
</section>

<section class="abs services" role="img" aria-label="Photo of a dentist treating a patient">
  <svg class="abs" style="left:0;top:-1px" width="1200" height="40" viewBox="0 0 1200 40" preserveAspectRatio="none"><path fill="#fff" d="M0 0 L1200 0 L1200 4 Q600 40 0 0 Z"/></svg>
  <h2>OUR SERVICES</h2>
  <div class="rule white" style="left:240px;top:272px"></div>
  <p>Sed ut perspiciatis unde omnis iste natus error sit voluptatem accusantium doloremque tium, totam rem aperiam, eaque ipsa quae ab illo tore veritatis et quasi architecto beatae vitae dicta sunt explicabo.</p>
  <a class="btn" style="left:184px;top:486px;width:164px;height:47px">Read More <i class="dot"></i></a>
  <div class="tile" style="left:563px;top:120px">
    <svg width="60" height="70" viewBox="0 0 60 70" fill="none" stroke="#fff" stroke-width="3"><path d="M15 5c-9 0-12 9-10 20 2 10 5 14 6 25 1 10 3 15 7 15 5 0 5-15 12-15s7 15 12 15c4 0 6-5 7-15 1-11 4-15 6-25 2-11-1-20-10-20-7 0-9 4-15 4S22 5 15 5z"/></svg>
    <span>Cleaning and prevention</span></div>
  <div class="tile" style="left:850px;top:120px">
    <svg width="60" height="70" viewBox="0 0 60 70" fill="none" stroke="#fff" stroke-width="3"><path d="M18 25c-6 0-8 6-7 13 1 7 3 9 4 16 1 6 2 10 5 10s3-9 10-9 7 9 10 9 4-4 5-10c1-7 3-9 4-16 1-7-1-13-7-13-5 0-6 3-12 3s-7-3-12-3zM4 40L18 8h24l14 32"/></svg>
    <span>Cosmetic dentistry</span></div>
  <div class="tile" style="left:563px;top:384px">
    <svg width="60" height="70" viewBox="0 0 60 70" fill="none" stroke="#fff" stroke-width="3"><path d="M18 4h24c4 0 6 4 5 9-1 4-6 6-17 6S14 17 13 13c-1-5 1-9 5-9zM22 24h16M22 32h16M23 40h14M25 48h10M27 56h6l-3 10z"/></svg>
    <span>Implant dentistry</span></div>
  <div class="tile" style="left:850px;top:384px">
    <svg width="60" height="70" viewBox="0 0 60 70" fill="none" stroke="#fff" stroke-width="3"><circle cx="22" cy="18" r="10"/><path d="M26 34c-5 0-7 5-6 11 1 6 3 8 3 13 1 5 2 8 4 8s3-7 8-7 5 7 8 7 4-3 4-8c1-5 3-7 4-13 1-6-1-11-6-11-4 0-5 2-10 2s-5-2-9-2z"/></svg>
    <span>Removable dentures</span></div>
  <svg class="abs" style="left:0;top:712px" width="1200" height="40" viewBox="0 0 1200 40" preserveAspectRatio="none"><path fill="#fff" d="M0 40 L0 38 Q600 -20 1200 38 L1200 40 Z"/></svg>
</section>

<section class="tips">
  <div class="abs" style="left:78px;top:2260px;width:296px;height:212px;background:var(--blue-mid)"></div>
  <div class="abs" style="left:371px;top:2088px;width:296px;height:210px;background:var(--teal)"></div>
  <div class="photo" style="left:92px;top:2100px;width:566px;height:359px;background:linear-gradient(120deg,#dfe6ec,#b8c7d2 50%,#e8d6dc)" role="img" aria-label="Photo of a dentist examining a smiling patient"></div>
  <h2 style="left:715px;top:2085px;color:var(--ink)">HEALTH TIPS</h2>
  <div class="rule" style="left:715px;top:2169px"></div>
  <p>At vero eos et accusamus et iusto odio dignissimos ducimus qui blanditiis praesentium voluptatum deleniti atque corrupti quos dolores et quas molestias excepturi sint occaecati cupiditate non provident, similique sunt in culpa qui officia deserunt mollitia animi.</p>
  <a class="btn" style="left:715px;top:2412px;width:165px;height:48px">Click Here <i class="dot"></i></a>
</section>

<section class="abs offer">
  <div class="abs" style="left:660px;top:0;width:540px;height:650px;background:radial-gradient(ellipse at 55% 50%,rgba(20,90,110,.35),rgba(0,0,0,0) 70%)" role="img" aria-label="Photo of a smiling woman in a dental chair"></div>
  <svg class="abs" style="left:0;top:-1px" width="1200" height="40" viewBox="0 0 1200 40" preserveAspectRatio="none"><path fill="#fff" d="M0 0 L1200 0 L1200 38 Q600 -10 0 2 Z"/></svg>
  <h2>NEW PATIENT OFFER</h2>
  <div class="rule white" style="left:90px;top:217px"></div>
  <p>At vero eos et accusamus et iusto odio dignissimos ducimus qui blanditiis praesentium voluptatum deleniti atque corrupti quos dolores et quas molestias excepturi sint occaecati cupiditate non provident, similique sunt in culpa qui officia deserunt mollitia animi.</p>
  <a class="btn" style="left:90px;top:458px;width:190px;height:48px;background:var(--blue)">Patient Portal <i class="dot"></i></a>
  <svg class="abs" style="left:0;top:612px" width="1200" height="40" viewBox="0 0 1200 40" preserveAspectRatio="none"><path fill="#fff" d="M0 40 L0 20 Q600 70 1200 10 L1200 40 Z"/></svg>
</section>

<section class="blog">
  <h2 style="top:3296px">BLOG</h2>
  <div class="rule" style="left:575px;top:3365px"></div>
  <svg class="abs" style="left:18px;top:3558px" width="28" height="14" viewBox="0 0 28 14"><path fill="var(--blue-mid)" d="M0 7l8-7v5h20v4H8v5z"/></svg>
  <svg class="abs" style="left:1154px;top:3558px" width="28" height="14" viewBox="0 0 28 14"><path fill="#555" d="M28 7l-8-7v5H0v4h20v5z"/></svg>
  <article class="card" style="left:90px;background:var(--blue-mid)">
    <div class="img" style="background:linear-gradient(135deg,#c9a58c,#e9e2d8 60%,#b9c9d6)" role="img" aria-label="Photo of a family talking with a doctor"></div>
    <h3>DIGNISSIMOS DUCIMUS</h3>
    <p>Lorem ipsum dolor sit amet, consectetur adipiscing elit, sed do eiusmod tempor</p>
  </article>
  <article class="card" style="left:439px;background:var(--teal)">
    <div class="img" style="background:linear-gradient(135deg,#e8ecf0,#9fb6cc 55%,#d7b9a2)" role="img" aria-label="Photo of a dentist with a child patient"></div>
    <h3>DIGNISSIMOS DUCIMUS</h3>
    <p>Lorem ipsum dolor sit amet, consectetur adipiscing elit, sed do eiusmod tempor</p>
  </article>
  <article class="card" style="left:787px;background:var(--blue-mid)">
    <div class="img" style="background:linear-gradient(135deg,#dfe6ec,#f3efe9 50%,#a7bccc)" role="img" aria-label="Photo of a doctor consulting with patients"></div>
    <h3>DIGNISSIMOS DUCIMUS</h3>
    <p>Lorem ipsum dolor sit amet, consectetur adipiscing elit, sed do eiusmod tempor</p>
  </article>
</section>

<footer class="abs footer">
  <svg class="abs" style="left:0;top:-1px" width="1200" height="44" viewBox="0 0 1200 44" preserveAspectRatio="none"><path fill="#fff" d="M0 0 L1200 0 L1200 40 Q600 -20 0 20 Z"/></svg>
  <div class="circle-btn" style="left:570px;top:22px">
    <svg width="22" height="22" viewBox="0 0 24 24" fill="none" stroke="var(--blue-mid)" stroke-width="2.5"><path d="M6 12l6-6 6 6M6 19l6-6 6 6"/></svg>
  </div>
  <div class="brand" style="left:449px;top:136px">
    <div class="mark" style="width:62px;height:58px"></div>
    <div style="font-size:30px">THE BRIGHTCREST<br>CLINIC</div>
  </div>
  <div class="fmenu"><span>HOME</span><span>MEET US</span><span>SERVICES</span><span>PATIENT INFO</span><span>CASES&amp;REVIEWS</span><span>BLOG</span><span>CONTACT</span></div>
  <div class="ficon" style="left:252px;background:var(--blue-mid)">
    <svg width="24" height="26" viewBox="0 0 24 26" fill="none" stroke="#fff" stroke-width="2"><path d="M12 24s8-8 8-14a8 8 0 00-16 0c0 6 8 14 8 14z"/><circle cx="12" cy="10" r="3"/></svg></div>
  <div class="ficon" style="left:570px;background:var(--teal)">
    <svg width="24" height="24" viewBox="0 0 24 24" fill="none" stroke="#fff" stroke-width="2"><path d="M6.6 10.8a15 15 0 006.6 6.6l2.2-2.2 5 1.6V20A17 17 0 014 4h3.6l1.6 5z"/></svg></div>
  <div class="ficon" style="left:890px;background:var(--blue-mid)">
    <svg width="26" height="20" viewBox="0 0 26 20" fill="none" stroke="#fff" stroke-width="2"><rect x="1" y="1" width="24" height="18"/><path d="M1 1l12 10L25 1"/></svg></div>
  <div class="finfo" style="left:131px">88 Harbor Lane, Suite<br>12, Fairview MA 01999</div>
  <div class="finfo" style="left:450px">555.014.2290</div>
  <div class="finfo" style="left:769px">info@brightcrestclinic-example.com</div>
  <div class="flinks">Help &nbsp;|&nbsp; Privacy Policy &nbsp;|&nbsp; Terms &amp; Services &nbsp;|&nbsp; Contact Us</div>
  <div class="copy">© 2019 Copyrights.The Company Name.All Rights Reserved</div>
  <div class="social" style="left:993px;top:557px"></div>
  <div class="social" style="left:1023px;top:557px"></div>
  <div class="social" style="left:1053px;top:557px"></div>
  <div class="social" style="left:1083px;top:557px"></div>
</footer>

</body>
</html>
```